Harbor Nightclub

Nightclub flyer., digital single sided, for KV and PX. I included samples of some previous flyers we've used. Sample Info:
HARBOR
FRIDAYS
FRI MAY 1 2020
DJ VORTAN (club floor)
DJ RUZO & DJ TAV (residents on the lounge floor)
4217 Marlow Avenue Sacramento
www.harborvenuehall.example for list/VIP inquiries

Target Market(s)

Upscale top 40 crowd but want some cool and artsy like the examples included.

Font styles to use
Sans Serif

Requirements
Must have
• Harbor Logo
Nice to have
• Would be nice if the flyer can be incorporated later with DJ photos (sometimes we will add dj photos to pixagram etc). Would like a big city type of feel.
Should not have
• Nothing too sexual.

```html
<!DOCTYPE html>
<html lang="en">
<head>
<meta charset="utf-8">
<title>Harbor Fridays</title>
<link rel="stylesheet" href="https://fonts.googleapis.com/css2?family=Oswald:wght@300;600&family=Righteous&family=Open+Sans:wght@400;600&family=PT+Sans&display=swap">
<style>
  :root {
    --page: #ffffff;
    --night: #231b47;
    --night-deep: #16112f;
    --glow-pink: #a8326f;
    --glow-violet: #5a2f9a;
    --neon-purple: #7c3aa6;
    --frame: #8f86b8;
    --white: #ffffff;
    --signal-red: #e3134a;
    --lime: #e4e43c;
    --hot-pink: #e0307f;
    --leaf: #a9d46c;
    --tri-glow: #9b6bff;
  }
  html, body {
    margin: 0;
    width: 1200px;
    height: 1200px;
    overflow: hidden;
    background: var(--page);
  }
  .flyer {
    position: absolute;
    left: 212px;
    top: 55px;
    width: 782px;
    height: 1107px;
    background:
      radial-gradient(ellipse 60% 12% at 50% 0%, rgba(200, 60, 140, 0.55), transparent 70%),
      radial-gradient(ellipse 30% 25% at 0% 42%, rgba(168, 50, 111, 0.45), transparent 70%),
      radial-gradient(ellipse 30% 25% at 100% 48%, rgba(90, 47, 154, 0.5), transparent 70%),
      linear-gradient(180deg, #2a1f52 0%, var(--night) 40%, var(--night-deep) 100%);
  }
  .flyer svg { position: absolute; inset: 0; }
  .frame { fill: none; stroke: var(--frame); stroke-width: 1; opacity: .8; }
  .venue { font-family: "Oswald", sans-serif; font-weight: 300; fill: var(--white); font-size: 50px; }
  .headline { font-family: "Righteous", sans-serif; font-size: 170px; fill: none; stroke: var(--neon-purple); stroke-width: 3.5; }
  .photo-slot { fill: url(#photoTone); }
  .neon-tri { fill: none; stroke: var(--white); stroke-width: 4; filter: url(#triGlow); }
  .date-day { font-family: "Oswald", sans-serif; font-weight: 600; font-size: 26px; fill: var(--white); }
  .date-num { font-family: "Oswald", sans-serif; font-weight: 600; font-size: 80px; fill: none; stroke: var(--signal-red); stroke-width: 4; }
  .date-year-box { fill: var(--signal-red); }
  .date-year { font-family: "Open Sans", sans-serif; font-weight: 600; font-size: 15px; fill: var(--white); letter-spacing: 6px; }
  .date-rule { stroke: var(--white); stroke-width: 1.5; opacity: .7; }
  .dj-name { font-family: "Righteous", sans-serif; font-size: 36px; fill: none; stroke: var(--lime); stroke-width: 1.6; }
  .dj-floor { font-family: "PT Sans", sans-serif; font-size: 23px; fill: var(--white); }
  .divider-tri { fill: none; stroke: var(--hot-pink); stroke-width: 2.5; }
  .dots { stroke: var(--white); stroke-width: 2; stroke-dasharray: 1.5 5; opacity: .8; }
  .address { font-family: "Open Sans", sans-serif; font-weight: 600; font-size: 36px; fill: var(--white); }
  .web { font-family: "Open Sans", sans-serif; font-size: 20px; fill: var(--leaf); }
</style>
</head>
<body>
<main class="flyer">
  <svg viewBox="0 0 782 1107" width="782" height="1107">
    <defs>
      <radialGradient id="photoTone" cx="50%" cy="45%" r="55%">
        <stop offset="0" stop-color="#6b3b3a"/>
        <stop offset=".45" stop-color="#2a1633"/>
        <stop offset="1" stop-color="#100b1e" stop-opacity="0"/>
      </radialGradient>
      <filter id="triGlow" x="-20%" y="-20%" width="140%" height="140%">
        <feGaussianBlur stdDeviation="5" result="b"/>
        <feFlood flood-color="#9b6bff"/>
        <feComposite in2="b" operator="in" result="g"/>
        <feMerge><feMergeNode in="g"/><feMergeNode in="g"/><feMergeNode in="SourceGraphic"/></feMerge>
      </filter>
    </defs>

    <rect class="frame" x="39" y="36" width="705" height="1031"/>

    <text class="venue" x="391" y="127" text-anchor="middle" textLength="272" lengthAdjust="spacing">HARBOR</text>
    <text class="headline" x="104" y="283" textLength="581" lengthAdjust="spacingAndGlyphs">FRIDAYS</text>

    <rect class="photo-slot" x="63" y="345" width="663" height="412" role="img" aria-label="Photo of a DJ at turntables and a mixer"/>
    <polygon class="neon-tri" points="563,347 146,545 449,753"/>

    <g class="event-date">
      <line class="date-rule" x1="583" y1="436" x2="711" y2="436"/>
      <text class="date-day" x="593" y="471" textLength="84" lengthAdjust="spacingAndGlyphs">FRIDAY</text>
      <text class="date-num" x="594" y="537" textLength="80" lengthAdjust="spacingAndGlyphs">01</text>
      <rect class="date-year-box" x="682" y="445" width="27" height="91"/>
      <text class="date-year" transform="translate(701 491) rotate(-90)" text-anchor="middle">2020</text>
      <line class="date-rule" x1="583" y1="550" x2="711" y2="550"/>
    </g>

    <g class="lineup">
      <text class="dj-name" x="63" y="855" textLength="250" lengthAdjust="spacingAndGlyphs">DJ VORTAN</text>
      <text class="dj-floor" x="188" y="884" text-anchor="middle">(club floor)</text>

      <polygon class="divider-tri" points="355,821 344,838 366,838"/>
      <polygon class="divider-tri" points="355,843 344,860 366,860"/>
      <polygon class="divider-tri" points="355,865 344,882 366,882"/>

      <text class="dj-name" x="391" y="855" textLength="328" lengthAdjust="spacingAndGlyphs">DJ RUZO &amp; DJ TAV</text>
      <text class="dj-floor" x="391" y="882" textLength="328" lengthAdjust="spacingAndGlyphs">(residents on the lounge floor)</text>
    </g>

    <line class="dots" x1="58" y1="913" x2="727" y2="913"/>
    <text class="address" x="81" y="961" textLength="613" lengthAdjust="spacingAndGlyphs">4217 MARLOW AVENUE SACRAMENTO</text>
    <line class="dots" x1="58" y1="992" x2="727" y2="992"/>

    <text class="web" x="99" y="1031" textLength="590" lengthAdjust="spacing">www.harborvenuehall.example for list/VIP inquiries</text>
  </svg>
</main>
</body>
</html>
```